Website Design - Photo Shop Design - Functional Cash Register Layout for POS System

Design a webpage for Point of Sale site. A cash register page.

Page must have a good look. I have attached a file of a possible layout example - but need a much nicer design. I have also attached the site logo. which i will upload without background tomorrow hopefully.

Looking for a nice Fresh look , not dark and dingy.

Target Market(s)

Business

Industry/Entity Type

Business Software

Number of Pages Required

1 page

Colors
f59195
f04a50
ec1f27
fbd4d5
ffffff
f8f3f8
fdf0f6
feeeee
ecf5f6

Requirements
Must have
• Cash register layout for POS software site. Nice layout ,
Nice to have
• Try putting he register part on the left side as well as the right - invert the designs have them different to the layout example shown too.
Should not have
• Not to dark

```html
<!DOCTYPE html>
<html lang="en">
<head>
<meta charset="utf-8">
<title>TillNimbus – Cash Register</title>
<link href="https://fonts.googleapis.com/css2?family=Lato:wght@300;400;700;900&family=Montserrat:wght@300;400;600&display=swap" rel="stylesheet">
<style>
:root{
  --red:#ec1f27;
  --red-soft:#f04a50;
  --canvas:#eceff4;
  --white:#ffffff;
  --ink:#1a1a1a;
  --line:#d4d7dc;
  --tile-coral:#f14a52;
  --tile-teal:#35bfb2;
  --tile-slate:#436f72;
  --tile-violet:#8f82e0;
  --tile-mustard:#e1c751;
  --tile-peach:#fea073;
  --avatar:#8a7a6c;
}
*{box-sizing:border-box;margin:0;padding:0}
html,body{width:1200px;height:575px;overflow:hidden}
body{position:relative;background:var(--canvas);font-family:"Lato",sans-serif;color:var(--ink)}
.abs{position:absolute}
.topbar{left:0;top:0;width:1200px;height:70px;background:var(--white);border-bottom:1px solid var(--line)}
.brand{left:22px;top:18px;display:flex;align-items:center;gap:8px;font-family:"Lato",sans-serif;font-weight:900;font-size:26px;color:var(--red);letter-spacing:-.5px}
.brand-mark{width:22px;height:22px;border-radius:50%;background:var(--red)}
.nav-link{top:26px;font-size:14px}
.avatar{left:904px;top:10px;width:49px;height:49px;border-radius:50%;background:radial-gradient(circle at 50% 40%,#c9b3a1,var(--avatar));border:1px solid var(--line)}
.register-name{left:962px;top:28px;font-size:11px;font-weight:700}
.hamburger{left:1159px;top:26px;width:20px;height:18px}
.hamburger span{display:block;height:3px;background:var(--red-soft);margin-bottom:4px;border-radius:1px}

.catalog{left:21px;top:88px;width:846px;height:406px;background:var(--white)}
.search{left:27px;top:17px;width:552px;height:40px;border:1px solid var(--line);border-radius:20px;display:flex;align-items:center;padding-left:15px;gap:14px;font-size:14px;color:#333}
.product{width:106px}
.product .swatch{height:105px;display:flex;align-items:center;justify-content:center;font-family:"Montserrat",sans-serif;font-weight:300;font-size:54px;color:var(--white)}
.product .name{height:25px;border:1px solid var(--line);border-top:none;font-size:11px;text-align:center;line-height:24px;white-space:nowrap;overflow:hidden;padding:0 4px}

.ticket{left:884px;top:88px;width:294px;height:406px;background:var(--white)}
.ticket-head{left:0;top:0;width:294px;height:61px;background:var(--red);color:var(--white)}
.customer{left:18px;top:22px;display:flex;align-items:center;gap:8px;font-size:13px;font-weight:700}
.txn{right:17px;top:14px;text-align:right;font-size:12px;line-height:17px}
.txn b{font-size:15px;font-weight:900}
.notes{left:18px;top:344px;font-size:13px;color:var(--red-soft)}
.totals{left:0;width:294px;top:366px;text-align:center;font-size:10px;line-height:20px}

.badge-slot{left:0;top:494px;width:263px;height:81px;background:var(--white)}
.badge{left:32px;top:16px;width:200px;height:50px;border-radius:8px;background:#e4e6ea}
.pill{top:517px;height:29px;border-radius:15px;background:var(--white);box-shadow:0 1px 2px rgba(0,0,0,.15);font-size:12.5px;display:flex;align-items:center;justify-content:center;letter-spacing:.2px}
.pill.active{background:var(--red);color:var(--white);font-weight:700}
.pager{left:651px;top:512px;height:32px;display:flex;border-radius:16px;overflow:hidden;box-shadow:0 1px 2px rgba(0,0,0,.15);background:var(--white)}
.pager span{width:31px;height:32px;display:flex;align-items:center;justify-content:center;font-size:13px;border-left:1px solid #e7e7e7}
.pager span:first-child{border-left:none;width:33px}
.pager span.current{background:var(--red);color:var(--white)}
.action{top:512px;height:32px;display:flex;align-items:center;font-size:11px;font-weight:700;color:var(--white)}
.add{left:885px;width:33px;background:var(--white);color:var(--ink);justify-content:center;font-size:16px;font-weight:400}
.park{left:918px;width:127px;background:#000;justify-content:center;letter-spacing:.2px}
.pay{left:1051px;width:127px;background:var(--red);justify-content:space-between;padding:0 9px 0 6px}
.pay b{font-size:14px}
</style>
</head>
<body>
<header class="abs topbar">
  <div class="abs brand"><span class="brand-mark"></span>TillNimbus</div>
  <span class="abs nav-link" style="left:820px">Backend</span>
  <div class="abs avatar" role="img" aria-label="Cashier profile photo"></div>
  <span class="abs register-name">My Shop / Cash Register</span>
  <span class="abs nav-link" style="left:1112px">Menu</span>
  <div class="abs hamburger"><span></span><span></span><span></span></div>
</header>

<main class="abs catalog">
  <div class="abs search">
    <svg width="17" height="17" viewBox="0 0 17 17"><circle cx="7" cy="7" r="5.3" fill="none" stroke="#000" stroke-width="2.6"/><line x1="11" y1="11" x2="15.5" y2="15.5" stroke="#000" stroke-width="2.8" stroke-linecap="round"/></svg>
    Search product by name or sku
  </div>
  <div class="abs product" style="left:29px;top:88px"><div class="swatch" style="background:var(--tile-coral)">DP</div><div class="name">Demo Product</div></div>
  <div class="abs product" style="left:254px;top:88px"><div class="swatch" style="background:var(--tile-teal)">EL</div><div class="name">Entry Level Comp...</div></div>
  <div class="abs product" style="left:479px;top:88px"><div class="swatch" style="background:var(--tile-slate)">GC</div><div class="name">Gift Card</div></div>
  <div class="abs product" style="left:706px;top:88px"><div class="swatch" style="background:var(--tile-violet)">PT</div><div class="name">Product Test</div></div>
  <div class="abs product" style="left:29px;top:247px"><div class="swatch" style="background:var(--tile-violet)">NP</div><div class="name">New Product</div></div>
  <div class="abs product" style="left:254px;top:247px"><div class="swatch" style="background:var(--tile-mustard)">PS</div><div class="name">Product Sales</div></div>
  <div class="abs product" style="left:479px;top:247px"><div class="swatch" style="background:var(--tile-coral)">LC</div><div class="name">Level Completed</div></div>
  <div class="abs product" style="left:706px;top:247px"><div class="swatch" style="background:var(--tile-peach)">TP</div><div class="name">Tested Product</div></div>
</main>

<aside class="abs ticket">
  <div class="abs ticket-head">
    <div class="abs customer">
      <svg width="14" height="15" viewBox="0 0 14 15"><circle cx="7" cy="4" r="3.6" fill="#fff"/><path d="M0 15c0-4.5 3-7 7-7s7 2.5 7 7z" fill="#fff"/></svg>
      Select Customer
    </div>
    <div class="abs txn">Transaction#<br><b>00016</b></div>
  </div>
  <div class="abs notes">Add Notes</div>
  <div class="abs totals">Subtotal: $0.00 | Tax: $0.00 | Disc: $0.00 | Total: $0.00<br>Paid: $0.00</div>
</aside>

<div class="abs badge-slot"><div class="abs badge" role="img" aria-label="App listing badge"></div></div>
<div class="abs pill active" style="left:283px;width:79px">LIST ALL</div>
<div class="abs pill" style="left:369px;width:70px">DEALS</div>
<div class="abs pill" style="left:447px;width:131px">UNCATAGORIZED</div>

<nav class="abs pager">
  <span><svg width="8" height="12" viewBox="0 0 8 12"><path d="M6.5 1.5L2 6l4.5 4.5" fill="none" stroke="#000" stroke-width="2"/></svg></span>
  <span class="current">1</span><span>2</span><span>3</span><span>4</span><span>5</span>
  <span><svg width="8" height="12" viewBox="0 0 8 12"><path d="M1.5 1.5L6 6l-4.5 4.5" fill="none" stroke="#000" stroke-width="2"/></svg></span>
</nav>

<div class="abs action add">+</div>
<div class="abs action park">SAVE &amp; PARK / LAYBY</div>
<div class="abs action pay"><span>PAY</span><b>$0.00</b></div>
</body>
</html>
```